Castellano Wine label**

Hi, we need a design for a white, red and sparkling wine label. We are a small italian restaurant (Castellano) and we want to release some wines under our personal brand. The restaurant has a rustic, italian provance style with with a slight modern, clean lines look. We would like a design that represent our mission to provide as authentic Italian food as we can, something that feels that it has been brought from the heart of Italy.
https://www.castellanotrattoria.ru/

```html
<!DOCTYPE html>
<html lang="en">
<head>
<meta charset="utf-8">
<title>Castellano Sangiovese Label</title>
<link rel="stylesheet" href="https://fonts.googleapis.com/css2?family=Josefin+Sans:wght@600&display=swap">
<style>
  :root {
    --ink: #0d0d0d;
    --white: #f6f4ef;
    --magenta: #d81b6e;
    --yellow: #f2d21b;
    --teal: #2bb3c0;
    --green: #6cc04a;
    --orange: #e8622a;
    --plum: #5a2a6e;
    --sky: #8fd0ea;
  }
  html, body {
    margin: 0;
    padding: 0;
    width: 750px;
    height: 1200px;
    overflow: hidden;
    background: var(--ink);
  }
  .label {
    position: relative;
    width: 750px;
    height: 1200px;
    overflow: hidden;
  }
  .label__pattern {
    position: absolute;
    inset: 0;
    width: 100%;
    height: 100%;
    display: block;
  }
  .label__panel {
    position: absolute;
    left: 50%;
    top: 430px;
    transform: translateX(-50%);
    width: 400px;
    height: 200px;
    box-sizing: border-box;
    background: var(--ink);
    display: flex;
    flex-direction: column;
    align-items: center;
    justify-content: center;
    gap: 24px;
  }
  .panel__name {
    margin: 0;
    display: flex;
    align-items: center;
    gap: 14px;
    font-family: "Josefin Sans", sans-serif;
    font-weight: 600;
    font-size: 44px;
    letter-spacing: 3px;
    color: var(--white);
    line-height: 1;
  }
  .panel__mark {
    width: 14px;
    height: 14px;
    background: var(--white);
    flex: none;
  }
  .panel__variety {
    margin: 0;
    font-family: "Josefin Sans", sans-serif;
    font-weight: 600;
    font-size: 24px;
    letter-spacing: 6px;
    color: var(--white);
    line-height: 1;
  }
</style>
</head>
<body>
  <main class="label">
    <svg class="label__pattern" viewBox="0 0 750 1200" preserveAspectRatio="none" role="img" aria-label="Colourful geometric pattern of interlocking triangles in magenta, yellow, teal, green, orange and plum">
      <defs>
        <linearGradient id="pattern-tones" x1="0" y1="0" x2="1" y2="1">
          <stop offset="0" stop-color="var(--orange)"/>
          <stop offset="0.18" stop-color="var(--magenta)"/>
          <stop offset="0.36" stop-color="var(--yellow)"/>
          <stop offset="0.52" stop-color="var(--teal)"/>
          <stop offset="0.68" stop-color="var(--green)"/>
          <stop offset="0.84" stop-color="var(--plum)"/>
          <stop offset="1" stop-color="var(--sky)"/>
        </linearGradient>
      </defs>
      <rect width="750" height="1200" fill="url(#pattern-tones)"/>
    </svg>

    <section class="label__panel">
      <h1 class="panel__name"><span class="panel__mark" aria-hidden="true"></span>Castellano</h1>
      <p class="panel__variety">SANGIOVESE</p>
    </section>
  </main>
</body>
</html>
```